New business outdoor sign design

We want to update our current Hotel sign to be modern design. We are open to ideas. The file that we upload is the size of the sign the blue sign is what we have now. We want completely new face look. Also there is also a backlight behind the face of the sign. Only words on sign we want is (4 Bells) we do not want the hotel part there. The sign company ask that it is done in vector art form. The design does NOT have to have a tree, we are open to all ideas, font styles. Be creative
Just a reminder the design does not have to have a tree, and you can use any font style. We are very open to any type of design.

```html
<!DOCTYPE html>
<html lang="en">
<head>
<meta charset="utf-8">
<title>4 Bells – Sign Face</title>
<link rel="stylesheet" href="https://fonts.googleapis.com/css2?family=Abril+Fatface&display=swap">
<style>
  :root {
    --backdrop-light: #d9d9d9;
    --backdrop-dark: #a9a9a9;
    --stone-light: #f2f3f1;
    --stone-mid: #e3e6e4;
    --stone-warm: #eadfcb;
    --gold-light: #f3e2a6;
    --gold-mid: #d9b45a;
    --gold-deep: #b8892b;
    --lettering-edge: #2a2318;
  }
  html, body {
    margin: 0;
    padding: 0;
    width: 1041px;
    height: 1200px;
    overflow: hidden;
  }
  body {
    background: linear-gradient(100deg, var(--backdrop-light) 0%, #c4c4c4 55%, var(--backdrop-dark) 100%);
  }
  .sign-canvas {
    display: block;
    width: 1041px;
    height: 1200px;
  }
  .sign-name {
    font-family: "Abril Fatface", "Times New Roman", serif;
    font-size: 230px;
    letter-spacing: 2px;
  }
</style>
</head>
<body>
<svg class="sign-canvas" viewBox="0 0 1041 1200" xmlns="http://www.w3.org/2000/svg">
  <defs>
    <linearGradient id="stoneFace" x1="0" y1="0" x2="1" y2="1">
      <stop offset="0" stop-color="var(--stone-warm)"/>
      <stop offset="0.25" stop-color="var(--stone-light)"/>
      <stop offset="0.6" stop-color="var(--stone-mid)"/>
      <stop offset="1" stop-color="var(--stone-light)"/>
    </linearGradient>
    <linearGradient id="goldLettering" x1="0" y1="0" x2="0" y2="1">
      <stop offset="0" stop-color="var(--gold-deep)"/>
      <stop offset="0.35" stop-color="var(--gold-mid)"/>
      <stop offset="0.6" stop-color="var(--gold-light)"/>
      <stop offset="1" stop-color="var(--gold-mid)"/>
    </linearGradient>
  </defs>

  <g class="sign-face">
    <path class="sign-panel" role="img" aria-label="White marble surface with soft gold veining"
          d="M80 406 Q520 326 960 406 L960 834 L80 834 Z"
          fill="url(#stoneFace)"/>
    <text class="sign-name" x="520" y="680" text-anchor="middle"
          fill="url(#goldLettering)" stroke="var(--lettering-edge)" stroke-width="4"
          paint-order="stroke">4 Bells</text>
  </g>
</svg>
</body>
</html>
```